Dentist's Office needs desktop and mobile website design

This is a turnkey project where we are looking for a bright, elegant, modern website design, both for desktop and mobile. Our existing website is hosted on Google sites. We also require the new design to be set up and fully functional - both desktop and mobile - on Google sites. If Google sites is too limiting, its ok to use a platform like Wix or Squarespace. If using these, we will need you to point our domain to the new Wix site, and hand us the credentials so we can continue to update the site.

We want to continue using our current logo so the new website colors need to go with the logo. Our existing website can be found at www.smilebay47.com.

We want the new website to have the following pages:
1. Home - similar content to our current home page at http://www.smilebay47.com

We also have pictures of our office and team that we would like to show up on the home page in a collage, slide show, or some other creative. Pictures can be found here: https://files.exampleshare.net/folderview?id=7KQ2MVRAXPL4hYwnBzTcLdEgHsJu&usp=sharing

Not all pictures have to be used; use as many as needed.

In addition to the content on our current home page, we would like a small section for dental quotes where we could rotate quotes. Sample quotes can be found at http://www.sayingsmeadow.net/dental.html

If above content is too much to fit on one page, it is ok to split into two.

2. Our team - similar to http://www.smilebay47.com/our-dentist-1 . In addition, we want short bios and pictures of other staff added to this page. Pictures and bios can be found here: https://files.exampleshare.net/folderview?id=7KQ2MVRAXPL4hYwnBzTcLdEgHsJu&usp=sharing

3. Reviews - similar to http://www.smilebay47.com/patient-testimonials-1

4. Services - provide a summary of services we provide from http://www.smilebay47.com/dental-services . No need for detailed pages pages for each treatment we have on our current website.

5. Contact Us - http://www.smilebay47.com/contact-us

Target Market(s)

local population

Industry/Entity Type

Healthcare

Coding

Coded - Design and coding required

Number of Pages Required

5+ page

Font styles to use
Sans Serif

Requirements
Nice to have
• animated icons would be cool

```html
<!DOCTYPE html>
<html lang="en">
<head>
<meta charset="utf-8">
<title>Sunvale Dental Care</title>
<link href="https://fonts.googleapis.com/css2?family=Open+Sans:ital,wght@0,300;0,400;0,600;0,700;1,400&family=Raleway:wght@300;400;600&display=swap" rel="stylesheet">
<style>
:root{
  --orange:#f08a24;
  --orange-dark:#d9741a;
  --blue:#2f9cc9;
  --text:#555;
  --muted:#8a8a8a;
  --line:#e3e3e3;
  --bg:#f4f4f4;
  --white:#fff;
}
*{box-sizing:border-box;margin:0;padding:0}
html,body{width:885px;height:1200px;overflow:hidden}
body{background:var(--bg);font-family:"Open Sans",Arial,sans-serif;color:var(--text);font-size:10px}
.page{position:relative;width:885px;height:1200px}
.wrap{width:790px;margin:0 auto;position:relative}
.site-header{height:100px;background:var(--white)}
.brand{position:absolute;left:260px;top:22px;display:flex;align-items:center;gap:10px}
.brand-dot{width:34px;height:34px;border-radius:50%;background:var(--orange)}
.brand-name{font-family:"Raleway",sans-serif;font-weight:600;font-size:26px;color:var(--orange)}
.contact{position:absolute;right:0;top:18px;text-align:right}
.contact .phone{font-size:20px;color:var(--blue);font-weight:300}
.contact .addr{font-size:9px;color:var(--muted);line-height:1.4}
.main-nav{background:var(--white);height:30px;border-top:1px solid var(--line);border-bottom:1px solid var(--line)}
.main-nav ul{list-style:none;display:flex;justify-content:center;gap:4px;height:100%;align-items:center}
.main-nav li{font-size:10px;color:var(--muted);padding:4px 10px}
.main-nav li+li{border-left:1px solid var(--line)}
.main-nav li.active{background:var(--orange);color:var(--white);border-radius:2px}
.hero{margin-top:12px;height:280px;background:var(--white);display:flex}
.hero-photo{width:420px;height:100%;background:linear-gradient(135deg,#cfe6f0,#8cc5dd 60%,#e9f2f6)}
.hero-copy{flex:1;padding:55px 30px 0 24px}
.hero-copy h1{font-family:"Raleway",sans-serif;font-weight:300;font-size:27px;line-height:1.15;color:var(--muted)}
.hero-copy h1 .accent{color:var(--orange)}
.hero-copy h1 strong{color:var(--blue);font-weight:400}
.hero-copy p{margin-top:14px;font-size:10px;line-height:1.6}
.hero-copy a{color:var(--orange);text-decoration:none}
.cards{margin-top:16px;display:flex;gap:14px;height:284px}
.card{flex:1;background:var(--white);text-align:center;display:flex;flex-direction:column}
.card h2{font-family:"Raleway",sans-serif;font-weight:300;font-size:19px;line-height:1.15;padding:22px 14px 0 16px;color:var(--blue);text-align:left;height:88px;flex:none}
.card h2 span{display:block;white-space:nowrap}
.card h2 .accent{color:var(--orange)}
.card-photo{height:110px;margin:0 16px;flex:none;background:linear-gradient(135deg,#dfe9ee,#b8d3df)}
.card p{font-size:8.5px;color:var(--muted);padding:10px 20px 0;line-height:1.5}
.card .small-link{font-size:8px;color:var(--muted);margin-top:10px}
.doctor-photo{height:150px;flex:none;background:linear-gradient(160deg,#efe8e2,#c9b4a6)}
.doctor-name{color:var(--orange);font-size:11px;font-weight:600;padding-top:10px}
.quote{height:80px;display:flex;align-items:center;justify-content:center;flex-direction:column;gap:6px}
.quote blockquote{font-family:"Raleway",sans-serif;font-style:italic;font-size:17px;color:var(--muted);display:flex;align-items:center;gap:12px}
.quote .mark{color:var(--orange);font-size:36px;font-style:normal;line-height:1}
.quote cite{font-style:normal;font-weight:700;font-size:11px;color:#444}
.testimonials{background:var(--orange);height:200px;color:var(--white)}
.testimonials h2{text-align:center;font-family:"Raleway",sans-serif;font-weight:400;font-size:22px;letter-spacing:2px;padding-top:16px}
.testimonials .rule{width:60px;height:2px;background:var(--white);margin:6px auto 14px}
.reviews{display:flex;gap:40px;width:620px;margin:0 auto}
.review{flex:1;display:flex;gap:12px}
.avatar{width:54px;height:54px;border-radius:50%;flex:none;background:linear-gradient(135deg,#f7d3b3,#e8a56e);border:2px solid var(--white)}
.review .date{font-size:8.5px;font-weight:600}
.review p{font-size:8.5px;line-height:1.5;margin-top:3px}
.review .who{font-size:8.5px;margin-top:4px;font-style:italic}
.members{height:140px;text-align:center;padding-top:14px}
.members h3{font-family:"Raleway",sans-serif;font-weight:400;font-size:15px;color:var(--muted)}
.badges{display:flex;justify-content:center;gap:90px;margin-top:12px}
.badge{width:120px}
.badge-shape{width:70px;height:46px;margin:0 auto;background:#d7dfe4;border-radius:4px}
.badge:nth-child(2) .badge-shape{background:#e9cfa8}
.badge:nth-child(3) .badge-shape{background:#c7d3e4}
.badge span{display:block;font-size:7.5px;color:var(--muted);margin-top:6px}
.site-footer{position:absolute;bottom:0;left:0;right:0;height:36px;border-top:1px solid var(--line);background:var(--white)}
.site-footer ul{list-style:none;display:flex;gap:8px;padding:12px 47px;font-size:8px;color:var(--muted)}
</style>
</head>
<body>
<div class="page">
  <header class="site-header">
    <div class="wrap">
      <div class="brand"><span class="brand-dot"></span><span class="brand-name">Sunvale Dental Care</span></div>
      <div class="contact">
        <div class="phone">555 014-2288</div>
        <div class="addr">12 Harbor Lane, Suite 4<br>Sunvale, CA 90000</div>
      </div>
    </div>
  </header>
  <nav class="main-nav">
    <ul>
      <li class="active">Home</li><li>Meet Our Doctor</li><li>Patient Testimonials</li><li>Dental Services</li><li>Insurance Plans</li><li>Financing</li><li>Specials</li><li>Contact Us</li>
    </ul>
  </nav>
  <div class="wrap">
    <section class="hero">
      <div class="hero-photo" role="img" aria-label="Photo of a smiling patient and dentist in the office"></div>
      <div class="hero-copy">
        <h1>It's our <span class="accent">genuine care &amp;</span><br><strong>gentle nature</strong><br>that sets us apart!</h1>
        <p>We want to provide you with everything you could want in a dental office: excellent care, a gentle nature, and a friendly staff – all in a comfortable location and at a great price. <a href="#">more...</a></p>
      </div>
    </section>
    <section class="cards">
      <article class="card">
        <h2><span>Weekend &amp; Emergency</span><span class="accent">Appointments</span></h2>
        <div class="card-photo" role="img" aria-label="Photo of the front desk"></div>
        <p>Weekend &amp; emergency appointments available</p>
        <div class="small-link">click for office hours</div>
      </article>
      <article class="card">
        <h2><span>New Patient</span><span class="accent">Specials</span></h2>
        <div class="card-photo" role="img" aria-label="Photo of a patient in the dental chair"></div>
        <p>Free exam and consultation for new patients, with affordable cleaning packages offered.</p>
        <div class="small-link">click for details</div>
      </article>
      <article class="card">
        <div class="doctor-photo" role="img" aria-label="Portrait of the dentist"></div>
        <div class="doctor-name">Dr Mira Sen</div>
        <p>Our dentist Dr Mira Sen is a skilled and caring practitioner, devoted to comfort, clear advice and gentle treatment for every patient who visits our office.</p>
      </article>
    </section>
    <section class="quote">
      <blockquote><span class="mark">“</span>A dentist at work in his vocation always looks down in the mouth.<span class="mark">”</span></blockquote>
      <cite>Harold P. Linwood</cite>
    </section>
  </div>
  <section class="testimonials">
    <h2>TESTIMONIALS</h2>
    <div class="rule"></div>
    <div class="reviews">
      <div class="review">
        <div class="avatar" role="img" aria-label="Patient photo"></div>
        <div>
          <div class="date">7 December 2014</div>
          <p>I've always been afraid of the dentist because of past visits. Our friend told us about this office and it changed my mind. I wouldn't go anywhere else. The staff is kind and careful.</p>
          <div class="who">– Patient Name</div>
        </div>
      </div>
      <div class="review">
        <div class="avatar" role="img" aria-label="Patient photo"></div>
        <div>
          <div class="date">3 June 2014</div>
          <p>Friendly team, short waits and clear answers every time. They explained each step and made my treatment easy. I recommend this office to my whole family and all my friends.</p>
          <div class="who">– Patient Name</div>
        </div>
      </div>
    </div>
  </section>
  <section class="members">
    <h3>Member of:</h3>
    <div class="badges">
      <div class="badge"><div class="badge-shape"></div><span>National Dental Guild</span></div>
      <div class="badge"><div class="badge-shape"></div><span>State Dental Society</span></div>
      <div class="badge"><div class="badge-shape"></div><span>Valley Dental Society</span></div>
    </div>
  </section>
  <footer class="site-footer">
    <ul><li>Sign in</li><li>|</li><li>Recent Site Activity</li><li>|</li><li>Report Abuse</li><li>|</li><li>Print Page</li></ul>
  </footer>
</div>
</body>
</html>
```